Delivery Docket urgent plus require many other designs for more stationary after this.

We need a new delivery docket design urgently as the one we have needs updating and we have changed our company name. Please do not copy the one I have uploaded as we do not feel this looks professional enough. I uploaded it as a few designers requested to see what we are currently using thank you.
It is quite complex in that we need a range of information to be on the one docket.
We are a Transport Company based in Australia that has a wide variety of items that we deliver such as water, sand and gravels and heavy equipment transport.
We would prefer to keep this design to A5 size as we will get them made into books. We are looking for a modern professional look. Although it is only a delivery docket this is given to all our customers so needs to look impressive.

We need our new logo on the docket (RWT). There will also need to be areas for our address and contact numbers, email etc these will be supplied to the winning designer to make the final adjustments so for now just put something generic in these spaces.
Needs to have an area for customer details, purchase order number, date and docket number (docket number to be in red)
Needs a section where we can list the type of product / and or service that has been provided and the amount / qty usually 3 lines will be enough for this. Need area under this where the customer can sign name and print name to say that the goods / and or services have been received.

Also required somewhere on the docket are the words, Tax Invoice will be issued based on the information provided on this docket. Conditions on back of page

We then need a separate section on the same page which we will use internally that the staff member can tear off and hand into the office. On this section it needs to have area where the driver can list km at start of job and at end with space to calculate km travelled, details of fuel purchased eg amount and litres, vehicle that is being used. also need to log down wheel bearing temps.
prime mover needs spaces as follows
Steer axel FL____________ Steer axel FR _________ 1st drive axel L_______
1st drive axel R_________ 2nd drive axel L_______ 2nd drive axel R________

For the trailers need something similar x 2 as have 2 trailers
1st axel DS_________ 1st axel PS_________ 2nd axel DS__________
2nd axel PS_________ 3rd axel DS_________ 3rd axel PS__________

I have included a few examples of designs we have used in past and ones that we like so you can get an idea of the colours we prefer, I have included some of the designs we are currently receiving for our logo that I like so you can get idea again of colours we prefer. There is much more we need designed also such as time sheets, more delivery dockets and letter heads so there is a lot of more work available to the winning designer.

Thank you

Target Market(s)

Customers

Font styles to use
Serif
Sans Serif

Colors

Designer to choose colors to be used in the design.

Requirements
Should not have
• Please don't copy old docket as we do not like it and nned new info on new design thank you

```html
<!DOCTYPE html>
<html lang="en">
<head>
<meta charset="utf-8">
<title>RWT Delivery Docket</title>
<link rel="stylesheet" href="https://fonts.googleapis.com/css2?family=Arimo:ital,wght@0,400;0,700;1,400&display=swap">
<style>
  :root {
    --page: #c3c3c3;
    --blue: #2f6db1;
    --slate: #7d95bd;
    --ink: #14213a;
    --black: #000;
    --red: #e0262b;
    --line: #2f6db1;
  }
  * { box-sizing: border-box; margin: 0; padding: 0; }
  html, body { width: 852px; height: 1200px; overflow: hidden; }
  body { background: var(--page); font-family: "Arimo", Arial, sans-serif; color: var(--ink); position: relative; }
  .abs { position: absolute; }

  .brand { left: 31px; top: 24px; width: 170px; height: 103px; display: flex; align-items: center; justify-content: center; font-size: 64px; font-weight: 700; color: var(--black); letter-spacing: 2px; }
  .company-address { left: 18px; top: 128px; width: 170px; text-align: center; font-size: 10px; line-height: 13.5px; color: var(--black); }

  .customer { left: 542px; top: 24px; width: 282px; height: 141px; border: 1.5px solid var(--line); border-radius: 10px; overflow: hidden; display: grid; grid-template-columns: 152px 1fr; grid-template-rows: 24px 28px 28px 30px 1fr; }
  .customer > div { border-bottom: 1px solid var(--line); font-size: 11px; padding: 3px 4px; color: var(--black); }
  .customer > div:nth-child(odd) { border-right: 1px solid var(--line); }
  .customer .head { background: var(--slate); font-weight: 700; font-size: 12px; display: flex; align-items: center; }
  .customer .docket { background: var(--blue); font-weight: 700; font-size: 9px; line-height: 9px; display: flex; align-items: center; gap: 6px; padding: 2px 4px; color: var(--ink); }
  .customer .docket .no { color: var(--red); font-size: 16px; }
  .customer .billing { grid-column: 1 / 3; border: none !important; }

  .items { left: 31px; top: 197px; width: 790px; height: 271px; border: 1.5px solid var(--line); border-radius: 11px; overflow: hidden; display: grid; grid-template-columns: 182px 421px 1fr; grid-template-rows: 56px 55px 55px 55px 1fr; }
  .items > div { border-right: 1px solid var(--line); border-bottom: 1px solid var(--line); }
  .items > div:nth-child(3n) { border-right: none; }
  .items > div:nth-last-child(-n+3) { border-bottom: none; }
  .items .col-head { display: flex; align-items: center; justify-content: center; font-size: 28px; font-weight: 700; color: var(--black); background: var(--slate); }
  .items .col-head.main { background: var(--blue); }

  .notice { left: 0; width: 852px; text-align: center; font-size: 19px; color: var(--black); }
  .notice.tax { top: 473px; font-style: italic; }
  .notice.cond { top: 498px; font-style: italic; }

  .receipt { left: 30px; top: 527px; width: 801px; height: 53px; background: var(--blue); border-radius: 11px; }
  .receipt .print { position: absolute; left: 0; top: 0; width: 290px; height: 53px; background: var(--slate); border-radius: 11px; font-size: 14px; padding: 3px 0 0 34px; color: var(--black); }
  .receipt .signed { position: absolute; left: 299px; top: 3px; font-size: 17px; color: var(--ink); }

  .tear-line { left: 10px; top: 597px; width: 832px; border-top: 2.5px dashed var(--blue); }

  .office-title { left: 30px; top: 628px; width: 801px; height: 53px; background: var(--blue); border-radius: 12px; display: flex; align-items: center; justify-content: center; font-size: 39px; font-weight: 700; color: var(--black); }

  .trip { left: 54px; top: 712px; width: 756px; height: 157px; border: 1.5px solid var(--line); border-radius: 10px; overflow: hidden; display: grid; grid-template-columns: 150px 110px 108px 43px 56px 31px 28px 149px 81px; grid-template-rows: 28px 27px 30px 30px 1fr; }
  .trip > div { border-right: 1px solid var(--line); border-bottom: 1px solid var(--line); }
  .trip .label { background: var(--blue); display: flex; align-items: center; justify-content: center; font-size: 15px; font-weight: 700; }
  .trip .incidences { background: var(--slate); font-size: 15px; font-weight: 700; padding: 2px 0 0 24px; border: none; }
  .trip .reviewed { background: var(--blue); font-size: 15px; font-weight: 700; padding: 2px 0 0 4px; border: none; }

  .pill { top: 912px; height: 40px; border-radius: 14px; background: var(--slate); display: flex; align-items: center; justify-content: center; font-size: 15px; font-weight: 700; }
  .pill.truck { left: 127px; width: 211px; }
  .pill.trailer { left: 521px; width: 213px; }

  .axles { top: 969px; width: 376px; height: 84px; border: 1.5px solid var(--line); border-radius: 10px; overflow: hidden; display: grid; grid-template-rows: repeat(3, 1fr); }
  .axles.truck { left: 42px; grid-template-columns: 89px 94px 85px 1fr; }
  .axles.trailer { left: 445px; grid-template-columns: 87px 95px 84px 1fr; }
  .axles > div { border-right: 1px solid var(--line); border-bottom: 1px solid var(--line); }
  .axles .label { background: var(--blue); font-size: 8.5px; font-weight: 700; display: flex; align-items: center; padding-left: 4px; }
  .axles.trailer .label { justify-content: center; padding-left: 0; }

  .signoff { left: 25px; top: 1097px; width: 806px; height: 55px; background: var(--blue); border-radius: 12px; font-size: 15px; font-weight: 700; }
  .signoff .reviewer { position: absolute; left: 0; top: 0; width: 255px; height: 55px; background: var(--slate); border-radius: 12px; padding: 7px 0 0 18px; }
  .signoff .date { position: absolute; left: 272px; top: 7px; }
  .signoff .driver { position: absolute; left: 551px; top: 0; width: 255px; height: 55px; background: var(--slate); border-radius: 12px; padding: 7px 0 0 20px; }
</style>
</head>
<body>
  <div class="abs brand">RWT</div>
  <div class="abs company-address">Depot House, 42.<br>Wattle Street.<br>Phone: 5550182<br>office@example.com</div>

  <div class="abs customer">
    <div class="head">COSTUMER DETAILS</div>
    <div class="docket"><span>DELIVERY<br>DOCKET</span><span class="no">000391</span></div>
    <div>NAME</div><div>DATE&nbsp;&nbsp;&nbsp;&nbsp;&nbsp;&nbsp;&nbsp;&nbsp;&nbsp;/&nbsp;&nbsp;&nbsp;&nbsp;&nbsp;&nbsp;/</div>
    <div>ORDER NUMBER</div><div></div>
    <div>CONTAC</div><div>PHONE</div>
    <div class="billing">BILLING ADDRESS</div>
  </div>

  <div class="abs items">
    <div class="col-head">Qty</div><div class="col-head main">Description</div><div class="col-head">Price</div>
    <div></div><div></div><div></div>
    <div></div><div></div><div></div>
    <div></div><div></div><div></div>
    <div></div><div></div><div></div>
  </div>

  <p class="abs notice tax">Tax Invoce will be based on information provided on this docket.</p>
  <p class="abs notice cond">Conditions on back of page</p>

  <div class="abs receipt">
    <div class="print">Goods received by (Print Name)</div>
    <div class="signed">SIGNED</div>
  </div>

  <div class="abs tear-line"></div>

  <div class="abs office-title">USE OF THE COMPANY</div>

  <div class="abs trip">
    <div class="label">VEHICLE</div><div style="grid-column: 2 / 4"></div>
    <div class="label" style="grid-column: 4 / 7">MODEL</div><div style="grid-column: 7 / 10"></div>

    <div class="label">SERIAL MOTOR</div><div style="grid-column: 2 / 4"></div>
    <div class="label" style="grid-column: 4 / 7">BODY SERIAL</div><div style="grid-column: 7 / 10"></div>

    <div class="label">STAR MILEAGE</div><div></div>
    <div class="label" style="grid-column: 3 / 5">FINAL MILEAGE</div><div style="grid-column: 5 / 7"></div>
    <div class="label" style="grid-column: 7 / 9">TRAVEL MILEAGE</div><div></div>

    <div class="label">FUEL PURCHASE</div><div></div>
    <div class="label" style="grid-column: 3 / 5">QUANTITY</div><div style="grid-column: 5 / 7"></div>
    <div class="label" style="grid-column: 7 / 9">PRICE</div><div></div>

    <div class="incidences" style="grid-column: 1 / 6">INCIDENCES</div>
    <div class="reviewed" style="grid-column: 6 / 10">REVIEWED BY</div>
  </div>

  <div class="abs pill truck">TRUCK INFORMATION</div>
  <div class="abs pill trailer">TRAILER INFORMATION</div>

  <div class="abs axles truck">
    <div class="label">STERR AXEL FL</div><div></div><div class="label">STERR AXEL FR</div><div></div>
    <div class="label">1ST DRIVE AXEL L</div><div></div><div class="label">1ST DRIVE AXEL R</div><div></div>
    <div class="label">2ND DRIVE AXEL L</div><div></div><div class="label">2ND DRIVE AXEL R</div><div></div>
  </div>

  <div class="abs axles trailer">
    <div class="label">1ST AXEL DS</div><div></div><div class="label">1ST AXEL PS</div><div></div>
    <div class="label">2ND AXEL DS</div><div></div><div class="label">2ND AXEL PS</div><div></div>
    <div class="label">3RT AXEL DS</div><div></div><div class="label">3RT AXEL PS</div><div></div>
  </div>

  <div class="abs signoff">
    <div class="reviewer">REVIEWED BY</div>
    <div class="date">DATE</div>
    <div class="driver">DRIVER</div>
  </div>
</body>
</html>
```